FAST TURNAROUND - simple sound/yoga event postcard

If you are up for a fast turnaround project within the next few hours then please submit your ideas. I have a photo, the text and a drawing of my idea for the front of the postcard.
PLEASE! Don't submit designs unless you are available now and can go back and forth to complete this project quickly -thank you-
PLEASE READ DETAILS FIRST - some designers are asking questions about things that I have outlined and specified in the brief -PLEASE LOOK AT ALL THE FILES - I have a doc about my ideas for the FRONT that are specific- thanks

FRONT OF THE POST CARD:
Please do not put anything else on the front other than the text on my instruction doc
I would like the lettering on the front of the card to be white or black (or white with black border) with simple fonts. However, I'm open to seeing the words WILLOW DRIFT in color blue for contrast
OPTION #1 for placing the title Willow Drift is to have the letter inside the gong (see my ideas for the front uploaded doc)
OPTION #2 for placing the title WILLOW DRIFT is the upper left part of the postcard.
lettering for lower left is Sound + Yogic Sleep (yoga nidra)

BACK OF THE POSTCARD:
BLACK BACKGROUND with white lettering. would love to see a couple of ideas of how you think the layout might look. I am open to only my website address being in blue as a contrast (or any of the other text) I've uploaded my logo but only on back side please keep it small
THANK YOU!

Target Market(s)

Yoga Students

Industry/Entity Type

Event

Requirements
Must have
• Must be 4.25 X 6.25 with bleed line CMYK - 300dpi PDF that follows the printers template (see uploaded files)
PLEASE READ INSTRUCTIONS ABOVE

Simple design please
Nice to have
• SEE ABOVE
Should not have
• LOGO NOT ON FRONT OF CARD
NO COLOR ON FRONT OF CARD JUST B AND W - maybe Willow Drift in color blue only

```html
<!DOCTYPE html>
<html lang="en">
<head>
<meta charset="utf-8">
<title>Willow Drift – Postcard Options</title>
<link href="https://fonts.googleapis.com/css2?family=Didact+Gothic&family=Nunito+Sans:wght@700&display=swap" rel="stylesheet">
<style>
  :root {
    --stage: #3b2a20;
    --card: #000000;
    --ink: #ffffff;
    --ink-soft: #d9d9d9;
    --link-blue: #3f5fc4;
    --accent-orange: #f28c1a;
    --label: #f2f2f2;
  }
  * { margin: 0; padding: 0; box-sizing: border-box; }
  html, body { width: 1200px; height: 1000px; overflow: hidden; }
  body {
    position: relative;
    background: var(--stage);
    font-family: "Didact Gothic", "Century Gothic", sans-serif;
    color: var(--ink);
  }
  .option-label {
    position: absolute;
    font-family: "Didact Gothic", sans-serif;
    font-size: 72px;
    line-height: 1;
    color: var(--label);
  }
  .card {
    position: absolute;
    background: var(--card);
    overflow: hidden;
    box-shadow: 0 6px 18px rgba(0,0,0,0.45);
  }
  .card--front-1 { left: 20px;  top: 118px; width: 578px; height: 385px; }
  .card--front-2 { left: 612px; top: 90px;  width: 578px; height: 385px; }
  .card--back-1  { left: 15px;  top: 597px; width: 579px; height: 384px; }
  .card--back-2  { left: 610px; top: 580px; width: 580px; height: 385px; }

  .gong-photo {
    position: absolute;
    inset: 0;
    background:
      radial-gradient(circle at 50% 50%, #2e2f33 0%, #3a3b3f 30%, #4b4b4d 48%, #6f6f70 56%, #8f8f8f 66%, #3a3a3a 88%, #111 100%);
  }
  .front-title {
    position: absolute;
    left: 30px; top: 28px;
    font-size: 30px;
    letter-spacing: 3px;
    color: var(--ink);
  }
  .front-arc { position: absolute; inset: 0; }
  .front-arc text {
    font-family: "Didact Gothic", sans-serif;
    font-size: 30px;
    letter-spacing: 9px;
    fill: var(--ink);
  }
  .front-tagline {
    position: absolute;
    left: 30px; bottom: 24px;
    font-family: "Nunito Sans", sans-serif;
    font-weight: 700;
    font-size: 13px;
    color: var(--ink);
  }

  .brand-mark {
    position: absolute;
    left: 0; right: 0;
    display: flex;
    align-items: center;
    justify-content: center;
    gap: 8px;
    font-size: 15px;
    letter-spacing: 2px;
    color: var(--ink);
  }
  .brand-mark__dot {
    width: 14px; height: 14px;
    border-radius: 50%;
    background: var(--accent-orange);
  }
  .web-address {
    position: absolute;
    left: 0; right: 0;
    text-align: center;
    font-size: 14px;
    letter-spacing: 5px;
    color: var(--link-blue);
  }
  .schedule { position: absolute; }
  .schedule__title { font-size: 14px; letter-spacing: 0.3px; }
  .schedule__venue { font-size: 7px; margin-top: 2px; color: var(--ink-soft); }
  .schedule__dates {
    font-size: 11.5px;
    line-height: 13px;
    letter-spacing: 0.3px;
  }
  .card--back-1 .schedule__dates {
    margin-top: 10px;
    padding-left: 5px;
    border-left: 1px solid #555;
  }
  .schedule-pair {
    position: absolute;
    left: 0; right: 0; top: 246px;
    display: flex;
    justify-content: center;
  }
  .schedule-pair .schedule { position: static; padding: 0 4px; }
  .schedule-pair .schedule--left { text-align: right; border-right: 1px solid #777; }
  .schedule-pair .schedule__dates { margin-top: 8px; }
</style>
</head>
<body>

  <div class="option-label" style="left:26px; top:58px;">1</div>
  <div class="option-label" style="left:1124px; top:34px;">2</div>
  <div class="option-label" style="left:26px; top:530px;">1</div>
  <div class="option-label" style="left:1124px; top:515px;">2</div>

  <!-- Front, option 1 -->
  <section class="card card--front-1">
    <div class="gong-photo" role="img" aria-label="Black and white photograph of a large ornate temple gong with eight small bosses around a central boss"></div>
    <h1 class="front-title">WILLOW DRIFT</h1>
    <p class="front-tagline">Sound + Yogic Sleep (yoga nidra)</p>
  </section>

  <!-- Front, option 2 -->
  <section class="card card--front-2">
    <div class="gong-photo" role="img" aria-label="Black and white photograph of a large ornate temple gong with eight small bosses around a central boss"></div>
    <svg class="front-arc" width="578" height="385" viewBox="0 0 578 385">
      <defs>
        <path id="title-arc" d="M 140 195 A 152 152 0 0 1 444 195"/>
      </defs>
      <text><textPath href="#title-arc" startOffset="50%" text-anchor="middle">WILLOW DRIFT</textPath></text>
    </svg>
    <p class="front-tagline">Sound + Yogic Sleep (yoga nidra)</p>
  </section>

  <!-- Back, option 1 -->
  <section class="card card--back-1">
    <div class="brand-mark" style="top:108px;"><span class="brand-mark__dot"></span>Mirabel Quinn</div>
    <p class="web-address" style="top:162px;">www.mirabelquinn.com</p>
    <div class="schedule" style="left:42px; top:248px;">
      <p class="schedule__title">Willow Drift dates:</p>
      <p class="schedule__venue">Lotus Grove -Hillside Studio (San Francisco)</p>
      <p class="schedule__dates">February 15, 2015<br>May 23rd, 2015<br>June 21st, 2015</p>
    </div>
    <div class="schedule" style="left:382px; top:248px;">
      <p class="schedule__title">Willow Drift dates:</p>
      <p class="schedule__venue">Lotus Grove-Canal Studio (San Francisco)</p>
      <p class="schedule__dates">February 28th, 2015<br>May 17th, 2015<br>June 6th, 2015</p>
    </div>
  </section>

  <!-- Back, option 2 -->
  <section class="card card--back-2">
    <div class="brand-mark" style="top:110px;"><span class="brand-mark__dot"></span>Mirabel Quinn</div>
    <p class="web-address" style="top:162px;">www.mirabelquinn.com</p>
    <div class="schedule-pair">
      <div class="schedule schedule--left">
        <p class="schedule__title">Willow Drift dates:</p>
        <p class="schedule__venue">Lotus Grove -Hillside Studio (San Francisco)</p>
        <p class="schedule__dates">February 15, 2015<br>May 23rd, 2015<br>June 21st, 2015</p>
      </div>
      <div class="schedule schedule--right">
        <p class="schedule__title">Willow Drift dates:</p>
        <p class="schedule__venue">Lotus Grove-Canal Studio (San Francisco)</p>
        <p class="schedule__dates">February 28th, 2015<br>May 17th, 2015<br>June 6th, 2015</p>
      </div>
    </div>
  </section>

</body>
</html>
```